At your fingertips

Our client specialising in selling EPoS (electronic tills) to the hospitality industry (restaurants, bars, hotels etc.)

We need a design (graphic) that we can use for an ad and a backdrop for a trade show booth. It needs to incorporate the logo (see attached) and it needs to capture the essence of our slogan 'Intelligent Hospitality...at your fingertips'

It needs to incorperate/display the followiong messages:

'Trageted marketing & loyalty solutions'

'Control wage costs and staff productivity'

Real-time multi-site management'

'Proven in over 800 hospitality establishments'

The design must not have technology in it e.g. no terminals, pcs etc, it should be nice and clean and project a corporate image, but also does not alianate independent operators

I have attached a design that we used last year - so something like this would be a clue as to what we are looking for.

Target Market(s)

Bar restarants hotels - both corprate (e.g. large chains) and independents e.g. local fine dining restuarants

Industry/Entity Type

Hospitality

Requirements
Must have
• Messages as described above

Logo must be incorporated (see attached)
Should not have
• technology

```html
<!DOCTYPE html>
<html lang="en">
<head>
<meta charset="utf-8">
<title>Tillway – Hospitality Messages</title>
<link rel="stylesheet" href="https://fonts.googleapis.com/css2?family=PT+Sans:wght@400;700&display=swap">
<style>
  :root {
    --crimson: #a5123f;
    --crimson-bright: #e0245a;
    --crimson-deep: #6e0a28;
    --panel-light: #ffffff;
    --panel-grey: #d4d4d4;
    --connector: #9a9a9a;
    --white: #ffffff;
  }
  html, body {
    margin: 0;
    padding: 0;
    width: 1200px;
    height: 900px;
    overflow: hidden;
  }
  .canvas {
    position: relative;
    width: 1200px;
    height: 900px;
    overflow: hidden;
    font-family: "PT Sans", "Trebuchet MS", sans-serif;
    background: linear-gradient(160deg, var(--crimson-bright) 0%, #c81a4c 45%, var(--crimson-deep) 100%);
    box-shadow: inset 0 0 0 6px #9c1238;
  }
  .backdrop-waves {
    position: absolute;
    inset: 0;
  }
  .message-panel {
    position: absolute;
    left: 37px;
    top: 37px;
    width: 1126px;
    height: 581px;
    background: linear-gradient(100deg, var(--panel-grey) 0%, #e6e6e6 40%, var(--panel-light) 75%, #f2f2f2 100%);
    box-shadow: 0 4px 14px rgba(60, 0, 20, 0.45);
  }
  .connectors {
    position: absolute;
    inset: 0;
  }
  .message {
    position: absolute;
    margin: 0;
    transform: translateX(-50%);
    white-space: nowrap;
    text-align: center;
    font-size: 38px;
    font-weight: 700;
    line-height: 44px;
    letter-spacing: 0.6px;
    color: var(--crimson);
    text-shadow: 3px 3px 4px rgba(0, 0, 0, 0.35);
  }
  .message--marketing { left: 293px; top: 165px; }
  .message--wages     { left: 823px; top: 108px; }
  .message--proven    { left: 878px; top: 316px; }
  .message--multisite { left: 308px; top: 375px; }

  .brand-name {
    position: absolute;
    left: 413px;
    top: 657px;
    width: 375px;
    height: 183px;
    display: flex;
    align-items: center;
    justify-content: center;
    margin: 0;
    font-size: 56px;
    font-weight: 700;
    letter-spacing: 3px;
    color: var(--white);
  }
</style>
</head>
<body>
<div class="canvas">
  <svg class="backdrop-waves" width="1200" height="900" viewBox="0 0 1200 900" aria-hidden="true">
    <path d="M0 640 C 300 560 700 700 1200 600 L1200 900 L0 900 Z" fill="#ffffff" opacity="0.06"/>
    <path d="M0 760 C 350 690 800 820 1200 720 L1200 900 L0 900 Z" fill="#5a0620" opacity="0.18"/>
    <path d="M700 900 C 850 760 1000 690 1200 660 L1200 900 Z" fill="#ffffff" opacity="0.07"/>
    <path d="M0 900 L0 700 C 150 760 260 840 320 900 Z" fill="#4a041a" opacity="0.25"/>
  </svg>

  <section class="message-panel" aria-label="Key messages">
    <svg class="connectors" width="1126" height="581" viewBox="0 0 1126 581" aria-hidden="true">
      <defs>
        <radialGradient id="pulse">
          <stop offset="0" stop-color="#d9305f"/>
          <stop offset="0.35" stop-color="#e0607f"/>
          <stop offset="0.55" stop-color="#eb98ab"/>
          <stop offset="0.7" stop-color="#e47a93"/>
          <stop offset="1" stop-color="#f2c0cc" stop-opacity="0"/>
        </radialGradient>
      </defs>
      <g fill="none" stroke="var(--connector)" stroke-width="4" stroke-linecap="round">
        <path d="M473 175 C 540 160 600 145 648 135"/>
        <path d="M1003 138 C 1110 140 1110 260 973 313"/>
        <path d="M273 258 C 170 300 125 350 138 408"/>
        <path d="M263 473 C 480 480 640 450 748 410"/>
      </g>
      <circle cx="88" cy="153" r="38" fill="url(#pulse)"/>
      <circle cx="623" cy="93" r="38" fill="url(#pulse)"/>
      <circle cx="683" cy="303" r="38" fill="url(#pulse)"/>
      <circle cx="81" cy="401" r="38" fill="url(#pulse)"/>
    </svg>

    <p class="message message--marketing">Targeted Marketing<br>and Loyalty Solutions</p>
    <p class="message message--wages">Control Wage Costs<br>and Staff Productivity</p>
    <p class="message message--proven">Proven in Over 800<br>Hospitality Establishments</p>
    <p class="message message--multisite">Real-Time<br>Multi-Site Management</p>
  </section>

  <p class="brand-name">TILLWAY</p>
</div>
</body>
</html>
```